Benefit Porter

Need home page design for new website. The winner will have the opportunity to design the entire site.

I have attached 3 files.

1) Sort of a site map. PLEASE do not design the home page based on this wire frame. Be creative and use your expertise.

2) Tagline and Copy for the home page. Please just greek in or make up copy for areas that do not have copy at this time.

3) The logo.
Updates

Hi everyone, I am sorry for the delay. I have been out of town on unexpected business. I will make a decision this week. Thank you all for the great designs. Dale

```html
<!DOCTYPE html>
<html lang="en">
<head>
<meta charset="utf-8">
<title>Benefit Porter — Home</title>
<link href="https://fonts.googleapis.com/css2?family=Roboto+Condensed:wght@400;700&family=Open+Sans:wght@400;600;700&family=Questrial&display=swap" rel="stylesheet">
<style>
:root{
  --page-bg:#f4f2ea;
  --white:#ffffff;
  --blue:#0b6a96;
  --navy:#0d4662;
  --green:#3bb44a;
  --green-dark:#2a9a3b;
  --grey-hero:#cdcdcd;
  --grey-panel:#ededed;
  --text:#333333;
  --muted:#666666;
  --rule:#d8d8d8;
}
*{box-sizing:border-box;margin:0;padding:0}
html,body{width:846px;height:1200px;overflow:hidden}
body{background:var(--page-bg);font-family:"Open Sans",sans-serif;color:var(--text);position:relative}
.abs{position:absolute}
.top-swoosh{left:0;top:0}
.page{left:64px;top:0;width:717px;height:1200px;background:var(--white)}

/* header */
.brand{left:93px;top:15px;display:flex;align-items:center;gap:10px}
.brand-dot{width:40px;height:40px;border-radius:50%;background:var(--blue)}
.brand-name{font-family:"Questrial",sans-serif;font-size:23px;color:var(--green)}
.social{left:640px;top:48px;display:flex;gap:3px}
.social span{width:20px;height:20px;background:#c9c9c9}
.social span:first-child{background:var(--navy)}
.nav-rule{left:93px;top:84px;width:659px;height:1px;background:var(--rule)}
.nav{left:93px;top:94px;width:667px;display:flex;justify-content:space-between;font-family:"Roboto Condensed",sans-serif;font-size:16.5px;color:#222}
.nav .current{color:var(--blue)}

/* hero */
.hero{left:64px;top:125px;width:717px;height:312px;background:var(--grey-hero)}
.hero-photo{left:64px;top:125px;width:360px;height:312px;background:linear-gradient(90deg,#bdbdbd,#8a8a8a 45%,#c4c4c4)}
.hero-title{right:124px;text-align:right;font-family:"Roboto Condensed",sans-serif;font-weight:700;line-height:1}
.t1{top:158px;font-size:56px;color:var(--green-dark);letter-spacing:-1px}
.t2{top:222px;font-size:38px;color:var(--navy)}
.t3{top:268px;font-size:41px;color:var(--green-dark)}
.hero-sub{right:124px;top:314px;text-align:right;font-family:"Questrial",sans-serif;font-size:17.5px;line-height:24px;color:#222}
.btn{font-family:"Open Sans",sans-serif;font-weight:700;font-size:14px;color:var(--white);display:flex;align-items:center;justify-content:center;height:28px}
.btn-demo{left:499px;top:377px;width:70px;background:var(--green)}
.btn-try{left:580px;top:377px;width:122px;background:var(--blue)}
.hero-arrow{top:248px}

/* welcome */
.section-title{font-family:"Roboto Condensed",sans-serif;font-size:15px;color:var(--blue);text-transform:uppercase}
.welcome-title{left:78px;top:456px}
.welcome-copy{left:78px;top:478px;width:455px;font-size:10.3px;line-height:16px}
.feature{width:150px;text-align:center}
.feature-icon{width:70px;height:70px;border-radius:50%;margin:0 auto;display:flex;align-items:center;justify-content:center}
.feature h3{font-family:"Roboto Condensed",sans-serif;font-weight:400;font-size:15px;line-height:18px;margin-top:16px;color:#333}
.feature p{font-size:9px;line-height:14.5px;color:var(--muted);margin-top:10px;height:44px;overflow:hidden}
.more{font-size:10.5px;font-weight:700;color:#333;margin-top:13px;display:inline-flex;align-items:center;gap:4px}
.more.green{color:var(--green)}
.more.white{color:var(--white)}
.more.blue{color:var(--blue)}

/* seminars */
.seminars-title{left:78px;top:781px}
.event{width:128px}
.event-photo{height:88px;background:linear-gradient(180deg,#9fc2dc 0%,#7fa861 45%,#4f7d2f 100%)}
.event h4{font-size:11px;font-weight:600;color:var(--blue);margin-top:10px}
.event p{font-size:9px;line-height:13px;color:var(--muted);margin-top:3px}
.event time{display:block;font-size:9px;color:var(--green-dark);margin-top:9px}

/* sidebar */
.holidays{left:570px;top:459px;width:211px;height:179px;background:var(--blue);color:var(--white)}
.holidays h3{position:absolute;left:15px;top:14px;font-family:"Roboto Condensed",sans-serif;font-weight:400;font-size:15px}
.holidays p{position:absolute;left:15px;top:42px;width:100px;font-size:10px;line-height:18.5px}
.holidays-photo{position:absolute;left:117px;top:44px;width:94px;height:94px;background:linear-gradient(180deg,#c8d6e2,#9aa8a0 55%,#707a78)}
.holidays .more{position:absolute;left:15px;top:149px;margin:0}
.blog{left:570px;top:659px;width:211px;height:152px;background:var(--grey-panel)}
.blog h3{position:absolute;left:15px;top:12px;font-family:"Roboto Condensed",sans-serif;font-weight:400;font-size:15px;color:var(--blue)}
.blog .subscribe{position:absolute;right:8px;top:15px;font-size:8.5px;display:flex;gap:3px;align-items:center}
.blog a{position:absolute;left:15px;top:51px;font-size:10px;color:var(--blue);text-decoration:underline}
.blog time{position:absolute;left:15px;top:67px;font-size:9.5px;font-style:italic}
.blog p{position:absolute;left:15px;top:92px;width:190px;font-size:8px;line-height:14px}
.blog p u{color:var(--blue)}
.blog .more{position:absolute;left:15px;top:127px;margin:0}
.stay{left:570px;top:812px;width:211px;height:156px;background:var(--grey-panel);border-top:1px solid #e0e0e0}
.stay h3{position:absolute;left:15px;top:15px;font-family:"Roboto Condensed",sans-serif;font-weight:400;font-size:15px;line-height:18px;color:var(--blue)}
.field{position:absolute;width:87px;height:23px;background:var(--white);border:1px solid #d2d2d2;font-size:9px;color:#555;padding:6px 0 0 14px}
.signup{position:absolute;left:15px;top:119px;width:71px;height:23px;background:var(--blue);color:var(--white);font-size:11px;font-weight:700;display:flex;align-items:center;justify-content:center}

/* footer */
.footer{left:64px;top:1011px;width:717px;height:189px;background:var(--green);color:var(--white)}
.menu-col{position:absolute;top:0}
.menu-col h4{font-family:"Open Sans",sans-serif;font-weight:600;font-size:13px;padding:12px 0 8px;border-bottom:1px solid rgba(255,255,255,.8);display:inline-block}
.menu-col ul{list-style:none;margin-top:8px;font-size:9.3px;line-height:18px}
.col-divider{position:absolute;top:36px;width:1px;height:106px;background:rgba(255,255,255,.6)}
.copyright{position:absolute;left:15px;top:161px;font-size:9.5px}
.contact-box{left:566px;top:997px;width:201px;height:198px;background:var(--blue);color:var(--white)}
.contact-brand{position:absolute;left:13px;top:14px;display:flex;align-items:center;gap:8px}
.contact-brand .dot{width:32px;height:32px;border-radius:50%;background:var(--white)}
.contact-brand span{font-family:"Questrial",sans-serif;font-size:17px}
.contact-box address{position:absolute;left:13px;top:63px;font-style:normal;font-size:10.5px;line-height:15px}
.contact-box .phones{position:absolute;left:13px;top:104px;font-size:10.5px}
.contact-box .email{position:absolute;left:13px;top:127px;font-size:10.5px}
.message-btn{position:absolute;left:14px;top:153px;width:152px;height:29px;background:var(--white);color:var(--blue);font-size:10.5px;display:flex;align-items:center}
.message-btn svg{margin:0 9px 0 9px}
.message-btn i{width:1px;height:20px;background:#bbb;margin-right:8px}
</style>
</head>
<body>
<svg class="abs top-swoosh" width="846" height="40" viewBox="0 0 846 40" aria-hidden="true">
  <path d="M380 0 C560 10 700 4 846 0 V26 C700 14 560 8 380 0Z" fill="var(--green)"/>
  <path d="M520 0 C650 4 760 10 846 22 V0Z" fill="var(--navy)"/>
  <path d="M0 0 H90 C60 2 30 3 0 4Z" fill="var(--green)"/>
</svg>

<div class="abs page"></div>

<header>
  <div class="abs brand"><span class="brand-dot"></span><span class="brand-name">BenefitPorter.com</span></div>
  <div class="abs social"><span></span><span></span><span></span><span></span><span></span></div>
  <div class="abs nav-rule"></div>
  <nav class="abs nav">
    <span class="current">Home</span><span>About Us</span><span>Pricing</span><span>Features</span><span>Services</span><span>Products</span><span>Conatct Us</span>
  </nav>
</header>

<section>
  <div class="abs hero"></div>
  <div class="abs hero-photo" role="img" aria-label="Black and white photo of three smiling children hugging"></div>
  <svg class="abs hero-arrow" style="left:78px" width="22" height="66" viewBox="0 0 22 66" aria-hidden="true"><path d="M20 2 L2 33 L20 64" fill="none" stroke="#999" stroke-width="1.5"/></svg>
  <svg class="abs hero-arrow" style="left:746px" width="22" height="66" viewBox="0 0 22 66" aria-hidden="true"><path d="M2 2 L20 33 L2 64" fill="none" stroke="var(--blue)" stroke-width="1.5"/></svg>
  <div class="abs hero-title t1">SUCCESSFUL</div>
  <div class="abs hero-title t2">NOT STRESSFUL</div>
  <div class="abs hero-title t3">FUNDRAISING</div>
  <p class="abs hero-sub">Charity Success, Minus the Stress<br>Sign Up Today for a Free Trial!</p>
  <a class="abs btn btn-demo">DEMO</a>
  <a class="abs btn btn-try">TRY FOR FREE</a>
</section>

<main>
  <h2 class="abs section-title welcome-title">Welcome to Benefit Porter</h2>
  <p class="abs welcome-copy">If you are thinking about having a fundraiser, there is no better and more popular event than charity golf.But the timeit takes to create invitations, registrations, banners, graphics, donors, as well as organizing and managing the entireevent can be quite off-putting.</p>

  <div class="abs feature" style="left:60px;top:542px">
    <div class="feature-icon" style="background:var(--blue)">
      <svg width="36" height="32" viewBox="0 0 36 32" aria-hidden="true"><path d="M18 29 C4 19 2 13 2 9 A7.5 7.5 0 0 1 18 6 A7.5 7.5 0 0 1 34 9 C34 13 32 19 18 29Z" fill="none" stroke="#fff" stroke-width="3"/><circle cx="27" cy="22" r="7" fill="#fff"/><rect x="23" y="21" width="8" height="2" fill="var(--blue)"/></svg>
    </div>
    <h3 style="color:var(--green-dark)">Raise More,<br>Stress Less</h3>
    <p>Charity golf events are proven to be an effective way to raise money for</p>
    <span class="more green">VIEW MORE <svg width="16" height="8" viewBox="0 0 16 8"><path d="M0 4H14M10 0.5L14.5 4L10 7.5" fill="none" stroke="currentColor" stroke-width="1.6"/></svg></span>
  </div>

  <div class="abs feature" style="left:228px;top:542px">
    <div class="feature-icon" style="background:#f4d433">
      <svg width="40" height="22" viewBox="0 0 40 22" aria-hidden="true"><path d="M2 6 H26 C32 6 36 3 38 5 C40 8 34 12 28 16 C24 19 16 19 2 19Z" fill="#fff"/></svg>
    </div>
    <h3>Everything you<br>need in one place</h3>
    <p>We are experienced in both the art of fundraising as well as the dynamics of a golf</p>
    <span class="more">VIEW MORE <svg width="16" height="8" viewBox="0 0 16 8"><path d="M0 4H14M10 0.5L14.5 4L10 7.5" fill="none" stroke="currentColor" stroke-width="1.6"/></svg></span>
  </div>

  <div class="abs feature" style="left:398px;top:542px">
    <div class="feature-icon" style="background:var(--green)">
      <svg width="28" height="26" viewBox="0 0 28 26" aria-hidden="true"><path d="M14 1 L27 13 H23 V25 H17 V17 H11 V25 H5 V13 H1Z" fill="#fff"/></svg>
    </div>
    <h3>Sold! Slient<br>Auction module</h3>
    <p>Exclusive to BenefitPorter.com is our Silent Auction module. Through our partners we can</p>
    <span class="more">VIEW MORE <svg width="16" height="8" viewBox="0 0 16 8"><path d="M0 4H14M10 0.5L14.5 4L10 7.5" fill="none" stroke="currentColor" stroke-width="1.6"/></svg></span>
  </div>

  <h2 class="abs section-title seminars-title">Seminars and Events</h2>
  <article class="abs event" style="left:79px;top:809px">
    <div class="event-photo" role="img" aria-label="Photo of golfers gathered on a course"></div>
    <h4>Lorem ipsum dolor sit</h4>
    <p>consectetur adipiscing elit. Quisque gravida</p>
    <time>14.06.2014</time>
  </article>
  <article class="abs event" style="left:247px;top:809px">
    <div class="event-photo" role="img" aria-label="Photo of a golf team posing on the green"></div>
    <h4>Lorem ipsum dolor sit</h4>
    <p>consectetur adipiscing elit. Quisque gravida</p>
    <time>14.06.2014</time>
  </article>
  <article class="abs event" style="left:415px;top:809px">
    <div class="event-photo" role="img" aria-label="Close-up photo of a golf club striking a ball on a tee"></div>
    <h4>Lorem ipsum dolor sit</h4>
    <p>adipiscing elit. Quisque gravida lobortis mollis</p>
    <time>14.06.2014</time>
  </article>
</main>

<aside>
  <div class="abs holidays">
    <h3>HIGH HOILYDAYS</h3>
    <p>Lorem ipsum dolor sit amet consectr adipiscing elitras portaarcu necorci accumsan.</p>
    <div class="holidays-photo" role="img" aria-label="Photo of a couple riding bicycles by the water"></div>
    <span class="more white">VIEW MORE <svg width="16" height="8" viewBox="0 0 16 8"><path d="M0 4H14M10 0.5L14.5 4L10 7.5" fill="none" stroke="currentColor" stroke-width="1.6"/></svg></span>
  </div>

  <div class="abs blog">
    <h3>BLOG FEEDS</h3>
    <span class="subscribe">Subscribe <svg width="9" height="9" viewBox="0 0 9 9"><circle cx="1.5" cy="7.5" r="1.3" fill="var(--blue)"/><path d="M1 4A4 4 0 0 1 5 8M1 1A7 7 0 0 1 8 8" fill="none" stroke="var(--blue)" stroke-width="1.3"/></svg></span>
    <a>Meet Benefit Porter : Lorem Ispum</a>
    <time>JULY 23, 2014</time>
    <p>But don’t put it off – PUTT it off! Benefit Porter. com is the helping hand you <u>Read More</u></p>
    <span class="more blue">VISIT BLOG <svg width="16" height="8" viewBox="0 0 16 8"><path d="M0 4H14M10 0.5L14.5 4L10 7.5" fill="none" stroke="currentColor" stroke-width="1.6"/></svg></span>
  </div>

  <div class="abs stay">
    <h3>LEARN ABOUT OUR WORK<br>&amp; STAY IN TOUCH</h3>
    <div class="field" style="left:15px;top:58px">First Name</div>
    <div class="field" style="left:109px;top:58px">Last Name</div>
    <div class="field" style="left:15px;top:88px">Email</div>
    <div class="field" style="left:109px;top:88px">Zip Code</div>
    <div class="signup">SIGN UP</div>
  </div>
</aside>

<footer class="abs footer">
  <div class="menu-col" style="left:15px">
    <h4>Menu</h4>
    <ul><li>Home</li><li>About us</li><li>Pricing</li><li>Features</li><li>Services</li><li>Products</li></ul>
  </div>
  <div class="col-divider" style="left:106px"></div>
  <div class="menu-col" style="left:151px">
    <h4>Quick Menu</h4>
    <ul><li>Get Involved</li><li>Donations</li><li>Child Sponsorship</li><li>Donations</li><li>Calendar</li><li>Our History</li></ul>
  </div>
  <div class="col-divider" style="left:280px"></div>
  <div class="menu-col" style="left:327px">
    <h4>Other Menu</h4>
    <ul><li>Support</li><li>Our Events</li><li>Donar</li><li>Rss Feeds</li><li>Policies Privacy</li><li>Site Map</li></ul>
  </div>
  <p class="copyright">Copyright ©2014 Benefit Porter. All rights reserved.</p>
</footer>

<div class="abs contact-box">
  <div class="contact-brand"><span class="dot"></span><span>BenefitPorter.com</span></div>
  <address>104955 Street Name, Ste 1000<br>Lom &nbsp;mipsum USA 900012</address>
  <p class="phones">123 456 7890 &nbsp;| &nbsp;123 456 7890</p>
  <p class="email">info@benefitporter.com</p>
  <div class="message-btn">
    <svg width="14" height="14" viewBox="0 0 14 14" aria-hidden="true"><path d="M1 13 L2 9 L10 1 L13 4 L5 12Z" fill="var(--blue)"/></svg>
    <i></i>SEND US A MESAAGE
  </div>
</div>
</body>
</html>
```